New Business Card for Casual Beachfront Cafe

Quirky Beachfront Cafe at Moana, South Australia needs a DOUBLE SIDED business card to print on PrintHarbor.

Target Market(s)

Business Cards sit on the counter for Guests to take with them. Please view our website www.saltreefcafe.com.au to get a feel for the Cafe. You may also view our Instagram at @saltreefcafe

Industry/Entity Type

Cafe / Restaurant

Contact Information for Business Card

Information equivalent to: Breakfast, Lunch, Dinner, Coffee, Takeaway / 117 Parade Kelpie Bay SA 5999 / Menu & Opening Hours: www.saltreefcafe.com.au / ph (08) 8461 9273

Requirements
Must have
• Information equivalent to: Breakfast, Lunch, Dinner, Coffee, Takeaway / 117 Parade Kelpie Bay SA 5999 / Menu & Opening Hours: www.saltreefcafe.com.au / ph (08) 8461 9273
Nice to have
• Potentially some of our trademark colours (Cafe can be searched via Seekly)
Should not have
• Must NOT have image of the building. May have the logo provided on one side but not necessarily, depending on how you wish to design the card

```html
<!DOCTYPE html>
<html lang="en">
<head>
<meta charset="utf-8">
<title>Salt Reef Cafe – Business Card</title>
<link rel="stylesheet" href="https://fonts.googleapis.com/css2?family=Lexend:wght@500;600;800&display=swap">
<style>
  :root {
    --paper: #ffffff;
    --sea-light: #dcecfb;
    --sea-surface: #62c4f3;
    --sea-mid: #0a86c4;
    --sea-deep: #075a86;
    --sea-floor: #0a3a5c;
    --sun-yellow: #f6ec10;
    --ink: #0b0b0b;
    --foam: #ffffff;
  }
  * { box-sizing: border-box; margin: 0; padding: 0; }
  html, body {
    width: 927px; height: 1200px; overflow: hidden;
    background: var(--paper);
    font-family: "Lexend", "Helvetica Neue", Arial, sans-serif;
  }
  .sheet { position: relative; width: 927px; height: 1200px; }
  .card {
    position: absolute; left: 105px; width: 679px; height: 424px;
    overflow: hidden;
  }
  .card--front { top: 148px; }
  .card--back { top: 624px; }
  .card__scene {
    position: absolute; inset: 0;
    background:
      radial-gradient(ellipse 45% 30% at 50% 22%, rgba(255,250,240,.9), rgba(255,255,255,0) 70%),
      linear-gradient(180deg, var(--sea-surface) 0%, var(--sea-light) 12%, #9fd6f5 20%, var(--sea-mid) 32%, var(--sea-deep) 65%, var(--sea-floor) 100%);
  }
  .card__frame {
    position: absolute; left: 12px; top: 9px; right: 10px; bottom: 12px;
    border: 2px solid var(--sun-yellow);
  }
  .contact {
    position: absolute; top: 29px; display: flex; align-items: center; gap: 7px;
    font-size: 23px; font-weight: 600; color: var(--ink); letter-spacing: .2px;
    white-space: nowrap;
  }
  .contact--web { left: 32px; }
  .contact--phone { right: 30px; }
  .contact svg { width: 27px; height: 27px; flex: none; }
  .brand {
    position: absolute; left: 0; right: 0; text-align: center;
    color: var(--sun-yellow); font-weight: 800; line-height: 1;
    text-transform: uppercase; white-space: nowrap;
  }
  .card--front .brand__top { top: 120px; font-size: 52px; letter-spacing: 1px; }
  .card--front .brand__bottom { top: 174px; font-size: 68px; letter-spacing: 2px; }
  .card--back .brand__top { top: 98px; font-size: 94px; letter-spacing: 2px; }
  .card--back .brand__bottom { top: 200px; font-size: 122px; letter-spacing: 4px; }
  .services {
    position: absolute; top: 250px; left: 0; right: 0; text-align: center;
    color: var(--foam); font-weight: 500; font-size: 35px; line-height: 43px;
  }
  .address-band {
    position: absolute; left: 47px; width: 592px; top: 356px; height: 44px;
    background: var(--sun-yellow); color: var(--ink);
    display: flex; align-items: center; justify-content: center;
    font-size: 31px; font-weight: 600; white-space: nowrap;
  }
</style>
</head>
<body>
<div class="sheet">

  <section class="card card--front">
    <div class="card__scene" role="img" aria-label="Underwater ocean scene with sunlight at the surface and seaweed silhouettes"></div>
    <div class="card__frame"></div>

    <div class="contact contact--web">
      <svg viewBox="0 0 28 28" fill="none" stroke="#0b0b0b" stroke-width="1.4" aria-hidden="true">
        <circle cx="14" cy="14" r="12"/>
        <ellipse cx="14" cy="14" rx="5" ry="12"/>
        <line x1="2" y1="14" x2="26" y2="14"/>
        <line x1="4" y1="8" x2="24" y2="8"/>
        <line x1="4" y1="20" x2="24" y2="20"/>
      </svg>
      <span>www.saltreefcafe.com.au</span>
    </div>

    <div class="contact contact--phone">
      <svg viewBox="0 0 28 28" fill="none" stroke="#0b0b0b" stroke-width="1.6" aria-hidden="true">
        <circle cx="14" cy="14" r="12"/>
        <path d="M10 7.5 l2.2 3 -1.4 1.6 c.9 2 2.4 3.6 4.4 4.6 l1.6-1.4 3 2.2 -1.4 2.3 c-5 -.4 -9.5 -5 -10 -10 z" fill="#0b0b0b" stroke-linejoin="round"/>
      </svg>
      <span>(08) 8461 9273</span>
    </div>

    <div class="brand brand__top">Salt Reef</div>
    <div class="brand brand__bottom">Cafe</div>

    <p class="services">Breakfast, Lunch, Dinner,<br>Coffee, Takeaway</p>

    <div class="address-band">117 Parade Kelpie Bay SA 5999</div>
  </section>

  <section class="card card--back">
    <div class="card__scene" role="img" aria-label="Underwater ocean scene with sunlight at the surface and seaweed silhouettes"></div>
    <div class="card__frame"></div>
    <div class="brand brand__top">Salt Reef</div>
    <div class="brand brand__bottom">Cafe</div>
  </section>

</div>
</body>
</html>
```